Varoden Imports Busisness cards and logo

Varoden imports is a brand new wholesale company located in Londonderry, New Hampshire dedicated to finding unique products from around the world.
Licensed to sell wine and spirits in the state and also authorized distributors of Blue Pepper Design, a manufacturer of girls and women shoes. Other products that we are currently trying to import are cheese and frozen food from Spain.
We would like a design that portraits our diversity of products and wholesale capabilities
Updates

Industry/Entity Type

It Company

```html
<!DOCTYPE html>
<html lang="en">
<head>
<meta charset="utf-8">
<title>Varoden Imports – Business Card</title>
<link href="https://fonts.googleapis.com/css2?family=Maven+Pro:wght@400;500;700&display=swap" rel="stylesheet">
<style>
  :root {
    --page-bg: #ece8e2;
    --card-blue-light: #1f5ea6;
    --card-blue: #1a4d8c;
    --card-blue-dark: #163f78;
    --band-navy: #1d2f63;
    --accent-orange: #f0901e;
    --name-orange: #f3a03a;
    --text-light: #dfe7f3;
    --text-white: #ffffff;
    --globe-light: #6fb2ec;
    --globe-dark: #1f6cc0;
  }
  * { box-sizing: border-box; margin: 0; padding: 0; }
  html, body {
    width: 1200px;
    height: 1024px;
    overflow: hidden;
    background: var(--page-bg);
    font-family: "Maven Pro", "Segoe UI", sans-serif;
  }
  .canvas {
    position: relative;
    width: 1200px;
    height: 1024px;
  }
  .business-card {
    position: absolute;
    left: 100px;
    top: 226px;
    width: 1000px;
    height: 572px;
    background: radial-gradient(ellipse at 40% 35%, var(--card-blue-light) 0%, var(--card-blue) 55%, var(--card-blue-dark) 100%);
    overflow: hidden;
    box-shadow: 0 10px 30px rgba(0,0,0,0.18);
  }
  .brand {
    position: absolute;
    left: 330px;
    top: 96px;
    display: flex;
    align-items: center;
    gap: 16px;
    white-space: nowrap;
  }
  .brand-dot {
    width: 16px;
    height: 16px;
    border-radius: 50%;
    background: var(--accent-orange);
  }
  .brand-name {
    font-weight: 700;
    font-size: 50px;
    letter-spacing: 1px;
    color: var(--accent-orange);
    text-transform: uppercase;
    line-height: 1;
  }
  .contact {
    position: absolute;
    left: 90px;
    top: 300px;
    color: var(--text-light);
    white-space: nowrap;
  }
  .contact-name {
    font-weight: 400;
    font-size: 46px;
    color: var(--name-orange);
    margin-bottom: 10px;
  }
  .contact-title,
  .contact-email {
    font-size: 22px;
    line-height: 1.4;
  }
  .contact-phone {
    font-size: 22px;
    font-weight: 500;
    color: var(--text-white);
    line-height: 1.5;
  }
  .globe-art {
    position: absolute;
    right: 40px;
    bottom: 50px;
    width: 200px;
    height: 200px;
    border-radius: 50%;
    background: radial-gradient(circle at 35% 35%, var(--globe-light) 0%, var(--globe-dark) 75%);
    z-index: 1;
  }
  .footer-band {
    position: absolute;
    left: 0;
    bottom: 22px;
    width: 100%;
    height: 66px;
    background: var(--band-navy);
    display: flex;
    align-items: center;
    padding-left: 90px;
    z-index: 2;
  }
  .postal-address {
    font-size: 19px;
    color: var(--text-light);
    letter-spacing: 0.3px;
    white-space: nowrap;
  }
  .footer-stripe {
    position: absolute;
    left: 0;
    bottom: 0;
    width: 100%;
    height: 22px;
    background: var(--accent-orange);
    z-index: 2;
  }
</style>
</head>
<body>
  <main class="canvas">
    <section class="business-card">
      <div class="brand">
        <span class="brand-dot"></span>
        <span class="brand-name">Varoden Imports</span>
      </div>

      <div class="contact">
        <p class="contact-name">Marco D Lerin</p>
        <p class="contact-title">V.P. of Sales</p>
        <p class="contact-email">mlerin2007@examplemail.net</p>
        <p class="contact-phone">207-555-0147</p>
      </div>

      <div class="globe-art" role="img" aria-label="Blue world globe with a golden curved arrow sweeping around it"></div>

      <div class="footer-band">
        <p class="postal-address">Postal Address: P.O. Box 418 Fairhaven, ME 04921-0418 USA</p>
      </div>
      <div class="footer-stripe"></div>
    </section>
  </main>
</body>
</html>
```